Best-selling author needs BOOK COVER DESIGN for "BRIGHT PUZZLES"

I need an impactful front and back cover design for my next non-fiction creative thinking book. Striking, modern, simple. Clean, with preference using black and red as dominant colours (but open to surprise).

Will be an e-book and printed book.
size; 6" x 9" (2:3 vertical rectangle)

barcode to come
some of the blurbs might change
insert author pic

Hope this is a great brief for you. Let me if any questions! ;)

Target Market(s)

Professionals. Maybe start-ups, entrepreneurs, or Fortune 500 execs

Industry/Entity Type

Business

Font styles to use
Serif
Sans Serif

Colors
f04a50
fece3e
fbee3e

Requirements
Must have
• FRONT COVER:
• title: BRIGHT PUZZLES
• subtitle: How to ask better questions to create breakthrough solutions.
• author name: Wren Tabor
• author descriptor: PANLx MC/Storyteller/Hothead
• review blurb: "The Perfect Storyteller!" - The Morning Ledger, UK.
• BACK COVER:
• title: Rock the New Economy with Explosive Questioning Skills.
• - Find out the Bright Puzzles that kick-started empires like NestLoop, Fenwick Dole, Brewhaven, Hydravolt, Sky Meridia, Lyrivo, Zintra, Orvello, Milo Grimsby, and, er, even FundSprout.
• - Learn how companies like T&W, Quince, Varnel, SkyTeal, Fablor, Lark, Valkor R9, Zumo, and Brex use Bright Puzzles to develop blockbuster new products, experiences and marketing messages.
• - How to identify and eradicate your cognitive blindspots.
• - How to create a Curiosity Gap (and why that’s so important).
• - Why it’s important to challenge the Status Quo and how to do it.
• title: What if there was a formula for creating Bright Puzzles? There is!
• Get on board this rocket ship with business creativity expert (and best-selling author) Wren Tabor as he guides us through a proven system for creating more insightful, more powerful questions, which point us toward breakthrough solutions, products, and process innovations.
• For the first time, he shares the Bright Puzzle (Innovation Question Formulation) System here. The same system that he has taught to senior executives from major corporations such as Norvabank, Trekko, HoltmannVeyr, Korvath, Medvane, and many other progressive companies.
• title: Praise for Wren Tabor’s work:
• “Really impressive and inspiring. Causes us to really jump out of the box. The questioning and challenging skills we learned here really apply to our everyday R&D work situations.” Derek PuyanSo, Senior Innovation Engineer, HoltmannVeyr.
• “Blown away! This is really corruptive to everything I’ve been thinking. I recommend this because it is so original.” Brent Ho, trekko.
• "Wren Tabor is truly a subject matter expert." Martin Oyo, Norvabank.
• www.wrentabor,example
Nice to have
• Book contents is workbooky and workshopy in style (ie alot about getting stuff up on flipcharts) so some 'handwritten' Inkdash marker type like in some attached examples might be suitable.
• does it need a graphic element? up to you
Should not have
• Not too busy, not too fussy. Simple and strong. Boom!
• Don't use Question Mark in cliched way

```html
<!DOCTYPE html>
<html lang="en">
<head>
<meta charset="utf-8">
<title>Bright Puzzles — Wren Tabor</title>
<link rel="stylesheet" href="https://fonts.googleapis.com/css2?family=Anton&family=Oswald:wght@400;500&family=PT+Sans+Narrow:wght@700&display=swap">
<style>
  :root {
    --cover-red: #ff0000;
    --band-yellow: #fbee2e;
    --wedge-orange: #f9ae3f;
    --ink-black: #0d0d0d;
    --descriptor-grey: #6b6b6b;
    --paper: #ffffff;
  }
  html, body {
    margin: 0;
    padding: 0;
    width: 799px;
    height: 1200px;
    overflow: hidden;
    background: var(--paper);
  }
  .book-cover {
    display: block;
    width: 799px;
    height: 1200px;
  }
  .review-band { fill: var(--band-yellow); }
  .review-quote {
    font-family: "Oswald", sans-serif;
    font-weight: 500;
    font-size: 35px;
    fill: var(--cover-red);
  }
  .review-source { font-weight: 400; }
  .cover-title {
    font-family: "Anton", sans-serif;
    font-size: 214px;
    fill: var(--cover-red);
  }
  .cover-subtitle {
    font-family: "PT Sans Narrow", sans-serif;
    font-weight: 700;
    font-size: 44px;
    fill: var(--ink-black);
  }
  .cover-artwork { fill: var(--wedge-orange); }
  .author-name {
    font-family: "PT Sans Narrow", sans-serif;
    font-weight: 700;
    font-size: 112px;
    fill: var(--ink-black);
  }
  .author-descriptor {
    font-family: "PT Sans Narrow", sans-serif;
    font-weight: 700;
    font-size: 37px;
    fill: var(--descriptor-grey);
  }
</style>
</head>
<body>
<svg class="book-cover" viewBox="0 0 799 1200" xmlns="http://www.w3.org/2000/svg">
  <rect class="review-band" x="0" y="0" width="799" height="82"/>
  <text class="review-quote" x="400" y="58" text-anchor="middle">“The Perfect Storyteller!”<tspan class="review-source"> - The Morning Ledger, UK.</tspan></text>

  <g class="cover-artwork" role="img" aria-label="Illustration of a head in profile struck by a red question mark, on an orange beam">
    <polygon points="668,502 799,502 799,1200 187,1200"/>
  </g>

  <text class="cover-title title-line-one" x="791" y="250" text-anchor="end" textLength="448" lengthAdjust="spacingAndGlyphs">BRIGHT</text>
  <text class="cover-title title-line-two" x="8" y="402" textLength="786" lengthAdjust="spacingAndGlyphs">PUZZLES</text>

  <text class="cover-subtitle" x="428" y="456" text-anchor="middle" textLength="646" lengthAdjust="spacingAndGlyphs">How to ask better questions to create</text>
  <text class="cover-subtitle" x="429" y="501" text-anchor="middle" textLength="402" lengthAdjust="spacingAndGlyphs">breakthrough solutions</text>

  <text class="author-name" x="25" y="1103" textLength="330" lengthAdjust="spacingAndGlyphs">Wren Tabor</text>
  <text class="author-descriptor" x="18" y="1156" textLength="382" lengthAdjust="spacingAndGlyphs">PANLx MC/Storyteller/Hothead</text>
</svg>
</body>
</html>
```